International professional tennis coach needs a book cover design

This is my 2nd published book, the first one was a #1 on the best seller. I'm looking for a world class book cover design for this new book. The name of my first book was 5 Baseline Habits to Unlock Your Rally Rhythm, located on Brimlow.com

The title of the new book:

Title: The Craft of Steady Rallies
Subtitle: Building a Tactical Margin by Way of Opponent Insight

I'm uploading our new CRAFT OF STEADY logo that I'd like for you to use as the centerpiece of the book design along with a 21st century design feel that incorporates what the book topic is below::

--> This book is about building competitive intelligence by using tennis data analytics to develop and expand a player's strategic advantage for match play. <--

The colors we would like to use are Blue, Yellow, and Green. These shades of these colors should be bold! (You will see the bold color examples of blues, yellows, and greens that I'm talking about in the logos that are attached here, especially the colors for my Tennis GridRally App logo.

I will upload the Tennis GridRally logo which should go somewhere on the back cover design (small size maybe in the bottom corner).

This book is revolutionary to the standard way of teaching tennis, it is based on a decade of recording and gathering tennis data analytics and then we created on-court practice games to develop better decision making in players for the competitive edge.

My websites are www.elevatedrillzone.com and www.craftofsteadyrallies.com

```html
<!DOCTYPE html>
<html lang="en">
<head>
<meta charset="utf-8">
<title>The Craft of Steady Rallies – Book Cover Wrap</title>
<link href="https://fonts.googleapis.com/css2?family=Lato:wght@300;400;700;900&family=Montserrat:wght@600;700&family=Oswald:wght@500;600&display=swap" rel="stylesheet">
<style>
  :root{
    --paper:#ffffff;
    --ink:#1d1d1b;
    --brand-blue:#2a62b4;
    --brand-yellow:#ffcc05;
    --green-light:#cfe12c;
    --green-mid:#9fd13a;
    --green-deep:#74bd43;
    --court-dark:#141414;
    --court-mid:#3a3a3a;
    --bleed:#f3b6c3;
    --trim:#111111;
  }
  *{box-sizing:border-box;margin:0;padding:0}
  html,body{width:853px;height:1200px;overflow:hidden;background:var(--paper)}
  body{position:relative;font-family:"Lato",sans-serif;color:var(--ink)}

  .cover-wrap{position:absolute;left:26px;top:314px;width:800px;height:572px;border:1px solid var(--bleed);overflow:hidden;background:var(--paper)}
  .trim-frame{position:absolute;left:8px;top:8px;right:8px;bottom:8px;border:1px solid var(--trim);z-index:10;pointer-events:none}
  .spine-fold{position:absolute;top:0;bottom:0;width:0;border-left:1px dashed var(--brand-blue);z-index:11}
  .spine-fold.left{left:379px}
  .spine-fold.right{left:421px}

  /* Back cover */
  .back-cover{position:absolute;left:0;top:0;width:379px;height:100%}
  .back-blurb{position:absolute;left:40px;top:43px;width:310px;font-size:7.9px;line-height:10.3px;text-align:justify;hyphens:auto}
  .back-blurb p{text-indent:8px;margin-bottom:4px}
  .author-band{position:absolute;left:0;top:267px;width:379px;height:206px;
    background:radial-gradient(circle at 25% 55%,var(--green-light) 0%,var(--green-mid) 45%,var(--green-deep) 100%)}
  .author{position:absolute;left:45px;width:304px;display:flex;gap:10px}
  .author.first{top:12px}
  .author.second{top:123px}
  .author-photo{width:77px;height:77px;flex:none;background:linear-gradient(160deg,#9aa0a6,#4b5057)}
  .author-bio{font-size:6.9px;line-height:10px;text-align:justify;text-indent:8px;color:#24331a}
  .author-bio strong{font-weight:700}
  .back-marks{position:absolute;left:41px;top:492px;display:flex;align-items:center;gap:22px}
  .partner-mark{display:flex;flex-direction:column;align-items:center;gap:3px}
  .partner-dot{width:22px;height:22px;border-radius:50%;background:var(--brand-blue)}
  .partner-name{font-family:"Montserrat",sans-serif;font-weight:700;font-size:6px;color:var(--green-deep);letter-spacing:.3px}
  .publisher-name{font-family:"Montserrat",sans-serif;font-weight:700;font-size:9px;color:var(--brand-blue)}

  /* Spine */
  .spine{position:absolute;left:379px;top:0;width:42px;height:100%}
  .spine-brand{position:absolute;left:50%;top:27px;transform:translateX(-50%);writing-mode:vertical-rl;
    font-family:"Montserrat",sans-serif;font-weight:700;font-size:6px;color:var(--brand-blue);letter-spacing:.3px}
  .spine-title{position:absolute;left:50%;top:80px;transform:translateX(-50%);writing-mode:vertical-rl;
    font-family:"Montserrat",sans-serif;font-weight:600;font-size:10.5px;letter-spacing:1px;color:var(--brand-blue);white-space:nowrap}

  /* Front cover */
  .front-cover{position:absolute;left:421px;top:0;width:379px;height:100%}
  .front-top{position:absolute;left:0;top:0;width:100%;height:222px;
    background:linear-gradient(200deg,var(--green-deep) 0%,var(--green-mid) 45%,var(--green-light) 100%)}
  .front-brand{position:absolute;right:34px;top:38px;text-align:right}
  .front-brand-name{display:flex;align-items:center;gap:4px;justify-content:flex-end;
    font-family:"Montserrat",sans-serif;font-weight:700;font-size:11px;color:var(--brand-blue)}
  .front-brand-dot{width:8px;height:8px;border-radius:50%;background:var(--brand-yellow)}
  .front-brand-url{font-size:4.4px;color:#fff;margin-top:5px;letter-spacing:.1px}
  .court-photo{position:absolute;left:0;top:222px;width:100%;height:258px;
    background:radial-gradient(ellipse at 40% 75%,var(--court-mid) 0%,#262626 40%,var(--court-dark) 100%)}
  .authors-line{position:absolute;left:15px;top:143px;width:263px;padding-bottom:4px;border-bottom:1.5px solid #fff;
    font-family:"Montserrat",sans-serif;font-weight:700;font-size:11.3px;color:var(--brand-blue);letter-spacing:.2px;white-space:nowrap}
  .title{position:absolute;left:15px;top:168px;z-index:2}
  .title-lead{font-weight:300;font-size:42px;line-height:44px;color:#fff;letter-spacing:-.5px;white-space:nowrap}
  .title-word{font-family:"Oswald",sans-serif;font-weight:600;font-size:80px;line-height:66px;letter-spacing:-1px;text-transform:uppercase}
  .title-word.steady{color:#fff;margin-top:10px}
  .title-word.rallies{color:var(--brand-yellow)}
  .subtitle{position:absolute;left:18px;top:501px;font-weight:700;font-size:16.5px;line-height:20.5px;color:var(--brand-blue)}
</style>
</head>
<body>
  <div class="cover-wrap">
    <section class="back-cover">
      <div class="back-blurb">
        <p>A practical guide on how to win more matches by becoming a more efficient and effective competitor.</p>
        <p>As a tennis player you have the ability to play better matches and win more of them. The Craft of Steady Rallies gives you a system to improve. We start with the individual game of the set itself. Our system examines your physical and mental progression, enabling you to upgrade your movement and performance from shot to shot and point to point. Our system seamlessly integrates the technical (physical) aspects with the tactical (mental/emotional) components, providing a comprehensive approach to elevate this performance.</p>
        <p>We aim to give you much more than how to hit great shots. Irrespective of your current skill level, we will provide you with a detailed strategic and tactical plan to enhance your performance, leading to improved results and increased success in your matches.</p>
        <p>The Craft of Steady Rallies emphasizes the importance of shifting focus from oneself to the opponent, encouraging players to analyze and understand their adversaries. By bringing the opponent back to the forefront of their thinking, the player creates the best possible context in which to improve as a competitor.</p>
        <p>In this book, we present a groundbreaking approach to tennis data analytics that seamlessly integrates match performance with practice sessions, and vice versa.</p>
      </div>

      <div class="author-band">
        <div class="author first">
          <div class="author-photo" role="img" aria-label="Portrait photo of author Merrick Vale"></div>
          <p class="author-bio"><strong>MERRICK VALE</strong> is regarded as one of the leading strategy and tactical coaches in the world today. He is the Creator of Tennis GridRally, the world's first Tennis Tracking App that maps and charts match play based on the rally length of a point. Merrick is a Best Selling Author of the book "5 Baseline Habits to Unlock Your Rally Rhythm" and the Co-Founder of The Craft of Steady Rallies promoting coach, player, and parent development. He is often sought after by coaches around the world to design the practice court in a way that revolutionizes a player's mindset to successfully negotiate the pressures of competitive match play.</p>
        </div>
        <div class="author second">
          <div class="author-photo" role="img" aria-label="Portrait photo of author Owen Hastings"></div>
          <p class="author-bio"><strong>OWEN HASTINGS</strong> is a writer and tennis coach. He is a Co-Founder at The Craft of Steady Rallies and has been working to create a theoretical framework for tennis players of all levels to improve. Owen studies the forces that act on the player during a tennis match (both internal and external) and works with players to meet the challenge these forces represent. He runs online and on court programs designed specifically to improve a player's Competitive Intelligence.</p>
        </div>
      </div>

      <div class="back-marks">
        <div class="partner-mark">
          <span class="partner-dot"></span>
          <span class="partner-name">TENNIS GRIDRALLY</span>
        </div>
        <span class="publisher-name">Craft of Steady</span>
      </div>
    </section>

    <section class="spine">
      <span class="spine-brand">Craft of Steady</span>
      <span class="spine-title">THE CRAFT OF STEADY RALLIES</span>
    </section>

    <section class="front-cover">
      <div class="front-top"></div>
      <div class="court-photo" role="img" aria-label="Photo of a yellow tennis ball resting on a dark court"></div>

      <div class="front-brand">
        <div class="front-brand-name"><span class="front-brand-dot"></span>Craft of Steady</div>
        <div class="front-brand-url">WWW.CRAFTOFSTEADYRALLIES.COM</div>
      </div>

      <p class="authors-line">MERRICK VALE &amp; OWEN HASTINGS</p>

      <h1 class="title">
        <span class="title-lead" style="display:block">THE CRAFT OF</span>
        <span class="title-word steady" style="display:block">Steady</span>
        <span class="title-word rallies" style="display:block">Rallies</span>
      </h1>

      <p class="subtitle">Building a Tactical Margin<br>by Way of Opponent Insight</p>
    </section>

    <div class="spine-fold left"></div>
    <div class="spine-fold right"></div>
    <div class="trim-frame"></div>
  </div>
</body>
</html>
```